Postcard / Online add graphic

I'm doing a campaign and need a single design that I can put into different formats. I can do that part, I just need the creative part done.

Title: Feed the Social Media Monster with Great Photography
Content: You can take the content from my website: http://www.brindlelenswork.com/business-branding-photography/

Sample Images: https://www.parcelvault.net/sh/k7m2qx9wbtrflzc/QRT3H8k2pwmXcDdLbvHUen_5r?dl=0

Here is a Monster image I licensed for use for this project: https://www.parcelvault.net/s/4hw7ncr2lpzqvkd/stockorbit_xxl_technologymosters.jpg?dl=0

Logo is attached

I want it to be fun, colorful, graphical, and attention getting. Cartoonish is ok.

Target Market(s)

Business owners, social media managers

Industry/Entity Type

Campaign

Font styles to use
Sans Serif

Requirements
Must have
• Title and design on front
• Sales copy on back (whatever fits)
• Contact Information: Wade Pellinger, Photographer, (555) 314-7720, www.brindlelenswork.com

```html
<!DOCTYPE html>
<html lang="en">
<head>
<meta charset="utf-8">
<title>Pellinger Photography – Postcard</title>
<link href="https://fonts.googleapis.com/css2?family=Kameron:wght@400;700&family=Lato:wght@400&display=swap" rel="stylesheet">
<style>
  :root {
    --page-bg: #e4e1dc;
    --card-white: #ffffff;
    --ink: #1f1f1f;
    --ink-soft: #3a3a3a;
    --panel-grey: #f1f1f1;
    --rule-grey: #c8c8c8;
    --dark-band: #1a1a1a;
    --dark-band-light: #4a4a4a;
    --ring-grey: #d9d9d9;
  }
  html, body { margin: 0; padding: 0; }
  body {
    width: 949px; height: 1200px; overflow: hidden;
    background: var(--page-bg);
  }
  .sheet {
    position: relative; width: 1121px; height: 1418px;
    transform: scale(0.84657); transform-origin: 0 0;
  }
  .card {
    position: absolute; left: 135px; width: 850px; height: 548px;
    background: var(--card-white); overflow: hidden;
    box-shadow: 0 4px 10px rgba(0,0,0,0.25);
  }
  .card--front { top: 115px; }
  .card--back { top: 715px; }
  .front-art { position: absolute; inset: 0; }
  .headline {
    position: absolute; left: 307px; top: 222px; width: 236px;
    margin: 0; text-align: center; color: #fff;
    font: 400 21px/33px "Kameron", serif;
  }
  .brand-name {
    position: absolute; left: 0; width: 850px; margin: 0; text-align: center;
    font-family: "Kameron", serif; font-weight: 400; color: var(--ink);
  }
  .card--front .brand-name { top: 448px; font-size: 34px; letter-spacing: 1px; }
  .front-contact {
    position: absolute; left: 0; top: 515px; width: 850px; margin: 0;
    text-align: center; font: 400 14px "Lato", sans-serif; color: var(--ink-soft);
    letter-spacing: 0.2px;
  }
  .back-copy {
    position: absolute; left: 0; top: 0; width: 448px; height: 452px;
    background: var(--panel-grey);
  }
  .back-band {
    position: absolute; left: 0; top: 0; width: 448px; height: 190px;
    background: radial-gradient(ellipse at 50% 20%, var(--dark-band-light), var(--dark-band) 75%);
  }
  .card--back .brand-name { width: 448px; top: 72px; font-size: 34px; color: #fff; letter-spacing: 1px; }
  .tagline {
    position: absolute; left: 0; top: 148px; width: 448px; margin: 0; text-align: center;
    font: 400 20px "Kameron", serif; color: #fff;
  }
  .tagline strong { font-weight: 700; }
  .copy-block { position: absolute; left: 29px; top: 203px; width: 405px; color: var(--ink); }
  .copy-block h2 { margin: 0 0 10px; font: 400 20px/27px "Kameron", serif; }
  .copy-block ul { margin: 0 0 16px; padding: 0; list-style: none; font: 400 14px/20.5px "Lato", sans-serif; color: var(--ink-soft); }
  .copy-block li { padding-left: 9px; text-indent: -9px; }
  .copy-block li::before { content: "• "; }
  .copy-block p { margin: 0; font: 400 14px/20px "Lato", sans-serif; color: var(--ink-soft); }
  .back-contact {
    position: absolute; left: 0; top: 470px; width: 448px; margin: 0; text-align: center;
    font: 400 14px/22px "Lato", sans-serif; color: var(--ink);
  }
  .stamp-box { position: absolute; left: 730px; top: 20px; width: 102px; height: 62px; border: 1px solid var(--rule-grey); }
  .address-line { position: absolute; left: 535px; width: 299px; height: 0; border-top: 1px solid var(--rule-grey); }
  .page-footer {
    position: absolute; left: 385px; top: 1398px; margin: 0;
    font: 400 14px "Lato", sans-serif; color: var(--ink-soft);
  }
</style>
</head>
<body>
<div class="sheet">

  <section class="card card--front">
    <svg class="front-art" viewBox="0 0 850 548" width="850" height="548">
      <defs>
        <linearGradient id="leftTone" x1="0" y1="0" x2="1" y2="1">
          <stop offset="0" stop-color="#2a2622"/><stop offset="0.5" stop-color="#5c4436"/><stop offset="1" stop-color="#181614"/>
        </linearGradient>
        <linearGradient id="midTone" x1="0" y1="0" x2="0" y2="1">
          <stop offset="0" stop-color="#aab4c6"/><stop offset="1" stop-color="#3f7a3a"/>
        </linearGradient>
        <linearGradient id="rightTone" x1="0" y1="0" x2="1" y2="1">
          <stop offset="0" stop-color="#141a24"/><stop offset="0.6" stop-color="#3a3d48"/><stop offset="1" stop-color="#2c64b8"/>
        </linearGradient>
        <radialGradient id="disc" cx="0.5" cy="0.3" r="0.7">
          <stop offset="0" stop-color="#555"/><stop offset="1" stop-color="#111"/>
        </radialGradient>
      </defs>
      <rect role="img" aria-label="Portrait photo of a smiling jewellery shop owner" x="0" y="0" width="430" height="548" fill="url(#leftTone)"/>
      <polygon role="img" aria-label="Photo of a smiling dry cleaner employee in a green shirt" points="150,0 700,0 425,275" fill="url(#midTone)"/>
      <polygon role="img" aria-label="Portrait photo of a smiling mechanic in a blue work shirt" points="700,0 850,0 850,548 425,275" fill="url(#rightTone)"/>
      <line x1="150" y1="-5" x2="425" y2="275" stroke="#fff" stroke-width="10"/>
      <line x1="700" y1="-5" x2="425" y2="275" stroke="#fff" stroke-width="10"/>
      <polygon points="0,548 425,235 850,548" fill="#fff"/>
      <circle cx="425" cy="275" r="120" fill="var(--ring-grey)"/>
      <circle cx="425" cy="275" r="110" fill="url(#disc)"/>
    </svg>
    <h1 class="headline">Feed the Social Media Monster with Great Photography</h1>
    <p class="brand-name">Pellinger Photography</p>
    <p class="front-contact">WADE PELLINGER, PHOTOGRAPHER &nbsp;|&nbsp; WWW.BRINDLELENSWORK.COM &nbsp;|&nbsp; (555) 314-7720</p>
  </section>

  <section class="card card--back">
    <div class="back-copy">
      <div class="back-band">
        <p class="brand-name">Pellinger Photography</p>
        <p class="tagline"><strong>Great Marketing</strong> starts with <strong>Great Images</strong></p>
      </div>
      <div class="copy-block">
        <h2>What can Business Branding Photography do for you?</h2>
        <ul>
          <li>It tells your uniqe story in fun, highly visual way</li>
          <li>Helps you engage with your customers on web, social media and print</li>
          <li>Sells more of your products or services</li>
        </ul>
        <h2>How does it work?</h2>
        <p>We book a photo shoot at one or more locations and take LOTS pictures</p>
      </div>
    </div>
    <p class="back-contact">WADE PELLINGER, PHOTOGRAPHER<br>(555) 314-7720<br>www.brindlelenswork.com</p>
    <div class="stamp-box"></div>
    <div class="address-line" style="top:249px"></div>
    <div class="address-line" style="top:289px"></div>
    <div class="address-line" style="top:330px"></div>
    <div class="address-line" style="top:371px"></div>
  </section>

  <p class="page-footer">WADE PELLINGER, PHOTOGRAPHER &nbsp;|&nbsp; WWW.BRINDLELENSWORK.COM &nbsp;|&nbsp; (555) 314-7720</p>
</div>
</body>
</html>
```